依頼詳細
マジックショーはステージがあります。
ショーの時間以外はテーブルマジックを行います。
堅い感じより柔らかい感じです。
楽しい、笑いのイメージ感です。
お店の広さは25坪くらいです。
まだ完成していませんが店内の写真添付します。
サイズを選ぶところがありますが、小さいのからある程度の大きさまでは印刷すると思います。

写真でロゴは添付しますが、データは決定した方に送りますので、その時に差し替えお願いします。
なので、案の時は何のフォントでもいいので入れ込んでください。
よろしくお願いします。
記載項目
順不同

奇術亭宇都宮店
2021年
1月18日グランドオープン

栃木県宇都宮市松原町2-5
梅川ビル2A
地図付けてください
028-3○○-1925(後ほど修正)
18時30分〜
定休日無し(不定休)
チラシ持参で500円OFF

毎日開催
ステージショーあり!
瞬き厳禁
テーブルマジックあり!

料金システム
フリータイム ¥2500(ワンドリンク制)
90分飲み放題付き¥3500
税別

楽しく元気になるお店
日本最大のエンターテイメント集団『奇術亭』がついに、宇都宮にオープン!
目の前で行われるプロのマジックと、ステージショーは必見!

#貸し切り#飲み放題#マジックショー#出張マジック
ハッシュタグみないに何個か思いつくのを入れるのもありかとも思っています。

とりあえずこんな的な感じです。それ以外の文言も入れてもらって構いませんし、こちらにある文章を変更していただいても構いません!

フライヤーを見て行ってみたいと思わせてくれるようなデザインに出会いたいです。

年末年始のタイミングでどれだけくるかわかりませんが、オープンが近いのでよろしくお願いします。
赤系、黄・オレンジ系、紫系
• 高解像度JPG (.jpg)
• イラストレーター形式 (.ai)
• フォトショップ形式 (.psd)
• PNG形式 (.png)
緊急事態宣言により、オープン日がズレました。
今後もどうなるかわからないので、日付を入れずにただのフライヤーで作成願います。
※今後も日付を入れる予定はないという事です。
■ 選んだ理由

スタッフでの多数決で決めさせて頂きました。

■ 提案者全員のお礼・コメント

たくさんのご応募ありがとうございました!

```html
<!DOCTYPE html>
<html lang="ja">
<head>
<meta charset="utf-8">
<title>奇術亭宇都宮店 フライヤー</title>
<link rel="stylesheet" href="https://fonts.googleapis.com/css2?family=Archivo+Black&family=Noto+Sans+JP:wght@400;700;900&display=swap">
<style>
  :root {
    --ink: #111111;
    --paper: #ffffff;
    --stage-dark: #0c0c10;
    --stage-red: #c8102e;
    --stage-glow: #ff3b3b;
    --accent-red: #d7141f;
    --soft-grey: #d9d9d9;
  }
  * { margin: 0; padding: 0; box-sizing: border-box; }
  html, body { width: 814px; height: 1200px; overflow: hidden; background: var(--paper); }
  body { font-family: "Noto Sans JP", sans-serif; color: var(--ink); }

  .flyer { position: relative; width: 814px; height: 1200px; background: var(--paper); overflow: hidden; }

  /* header */
  .header { position: absolute; left: 0; top: 0; width: 814px; height: 185px; }
  .header__tagline { position: absolute; left: 27px; top: 22px; font-size: 18px; font-weight: 700; letter-spacing: 0.5px; }
  .brand { position: absolute; left: 27px; top: 50px; }
  .brand__name { font-size: 78px; font-weight: 900; line-height: 1; letter-spacing: -2px; }
  .brand__roman { font-size: 14px; font-weight: 700; letter-spacing: 4px; margin-top: 6px; padding-left: 6px; }
  .branch-tag { position: absolute; left: 330px; top: 60px; width: 82px; height: 46px; border: 2px solid var(--ink); font-size: 19px; font-weight: 700; display: flex; align-items: center; justify-content: center; }
  .open-title { position: absolute; left: 430px; top: 30px; width: 370px; text-align: right; font-family: "Archivo Black", sans-serif; font-weight: 400; font-size: 104px; line-height: 1; letter-spacing: 2px; }

  /* stage area */
  .stage { position: absolute; left: 14px; top: 185px; width: 786px; height: 887px; background: var(--stage-dark); overflow: hidden; }
  .stage__art {
    position: absolute; inset: 0;
    background:
      radial-gradient(ellipse 180px 320px at 50% 45%, rgba(255,59,59,0.95), rgba(200,16,46,0.75) 55%, rgba(200,16,46,0) 100%),
      radial-gradient(ellipse 260px 60px at 50% 92%, rgba(255,80,80,0.7), rgba(255,80,80,0) 100%),
      linear-gradient(180deg, #15151c 0%, #0c0c10 60%, #2a0a10 100%);
  }

  .intro { position: absolute; left: 66px; top: 200px; width: 330px; color: var(--paper); }
  .intro__headline { display: inline-block; background: var(--paper); color: var(--ink); font-size: 32px; font-weight: 900; line-height: 1.3; padding: 8px 14px; }
  .intro__body { margin-top: 22px; font-size: 17px; line-height: 1.6; font-weight: 700; }

  .feature { position: absolute; right: 27px; text-align: right; color: var(--paper); }
  .feature__title { font-size: 34px; font-weight: 900; line-height: 1.2; }
  .feature__sub { font-size: 19px; font-weight: 700; margin-top: 4px; }
  .feature--stage { top: 205px; }
  .feature--table { top: 348px; }

  .pricing { position: absolute; left: 66px; top: 480px; width: 330px; color: var(--paper); }
  .pricing__label { font-size: 17px; font-weight: 700; margin-bottom: 8px; }
  .pricing__box { background: var(--paper); color: var(--ink); padding: 14px 16px; }
  .price-row { display: flex; align-items: baseline; justify-content: space-between; }
  .price-row + .price-row { margin-top: 12px; border-top: 1px solid var(--soft-grey); padding-top: 10px; }
  .price-row__name { font-size: 17px; font-weight: 700; }
  .price-row__amount { font-size: 34px; font-weight: 900; color: var(--accent-red); line-height: 1; }
  .price-row__note { display: block; font-size: 11px; color: var(--ink); text-align: right; font-weight: 700; }
  .tax-note { font-size: 11px; font-weight: 700; color: var(--ink); }

  .hashtags { position: absolute; right: 27px; top: 493px; width: 244px; background: var(--paper); padding: 8px 14px; list-style: none; }
  .hashtags li { font-size: 18px; font-weight: 700; padding: 7px 0; border-bottom: 1px solid var(--soft-grey); }
  .hashtags li:last-child { border-bottom: none; }

  /* footer */
  .footer { position: absolute; left: 0; top: 1072px; width: 814px; height: 128px; }
  .footer-brand { position: absolute; left: 36px; top: 12px; }
  .footer-brand__name { font-size: 70px; font-weight: 900; line-height: 1; letter-spacing: -2px; }
  .footer-brand__roman { font-size: 13px; font-weight: 700; letter-spacing: 4px; margin-top: 6px; padding-left: 6px; }
  .access-map { position: absolute; left: 298px; top: 10px; width: 176px; height: 108px; background: linear-gradient(135deg, #eeeeee, #d4d4d4); border: 1px solid #999; }
  .address { position: absolute; left: 488px; top: 8px; width: 305px; }
  .address__line { font-size: 14px; font-weight: 700; line-height: 1.3; }
  .address__phone { display: flex; align-items: center; gap: 6px; font-size: 22px; font-weight: 900; line-height: 1.15; margin-top: 1px; }
  .address__hours { font-size: 13px; font-weight: 700; line-height: 1.4; }
  .coupon { margin-top: 3px; height: 26px; background: var(--accent-red); color: var(--paper); font-size: 16px; font-weight: 900; line-height: 26px; text-align: center; }
</style>
</head>
<body>
<main class="flyer">

  <header class="header">
    <p class="header__tagline">日本最大のエンターテイメント集団</p>
    <div class="brand">
      <div class="brand__name">奇術亭</div>
      <div class="brand__roman">KIJUTSUTEI</div>
    </div>
    <div class="branch-tag">宇都宮店</div>
    <h1 class="open-title">OPEN</h1>
  </header>

  <section class="stage">
    <div class="stage__art" role="img" aria-label="スポットライトに照らされたステージと大きな赤いはてなマーク、周りに散らばるカラフルなはてなマークのイラスト"></div>

    <div class="intro">
      <h2 class="intro__headline">楽しく<br>元気になるお店</h2>
      <p class="intro__body">日本最大のエンターテイメント集団<br>「奇術亭」がついに、<br>宇都宮にオープン！<br>目の前で行われるプロのマジックと、<br>ステージショーは必見！</p>
    </div>

    <div class="feature feature--stage">
      <p class="feature__title">毎日開催</p>
      <p class="feature__sub">ステージショーあり！</p>
    </div>
    <div class="feature feature--table">
      <p class="feature__title">瞬き厳禁</p>
      <p class="feature__sub">テーブルマジックあり！</p>
    </div>

    <div class="pricing">
      <p class="pricing__label">料金システム</p>
      <div class="pricing__box">
        <div class="price-row">
          <span class="price-row__name">フリータイム</span>
          <span><span class="tax-note">税別</span> <span class="price-row__amount">¥2500</span><span class="price-row__note">（ワンドリンク制）</span></span>
        </div>
        <div class="price-row">
          <span class="price-row__name">90分 飲み放題付き</span>
          <span><span class="tax-note">税別</span> <span class="price-row__amount">¥3500</span></span>
        </div>
      </div>
    </div>

    <ul class="hashtags">
      <li>#貸し切り</li>
      <li>#飲み放題</li>
      <li>#マジックショー</li>
      <li>#出張マジック</li>
    </ul>
  </section>

  <footer class="footer">
    <div class="footer-brand">
      <div class="footer-brand__name">奇術亭</div>
      <div class="footer-brand__roman">KIJUTSUTEI</div>
    </div>
    <div class="access-map" role="img" aria-label="奇術亭宇都宮店周辺のアクセスマップ"></div>
    <div class="address">
      <p class="address__line">栃木県宇都宮市松原町2-5</p>
      <p class="address__line">梅川ビル2A</p>
      <p class="address__phone">
        <svg width="18" height="18" viewBox="0 0 24 24" aria-hidden="true"><path fill="#111" d="M6.6 10.8a15.1 15.1 0 0 0 6.6 6.6l2.2-2.2c.3-.3.7-.4 1-.2 1.1.4 2.3.6 3.6.6.6 0 1 .4 1 1V20c0 .6-.4 1-1 1A17 17 0 0 1 3 4c0-.6.4-1 1-1h3.5c.6 0 1 .4 1 1 0 1.3.2 2.5.6 3.6.1.3 0 .7-.2 1z"/></svg>
        028-3○○-1925
      </p>
      <p class="address__hours">18時30分〜　定休日無し（不定休）</p>
      <p class="coupon">チラシ持参で500円OFF</p>
    </div>
  </footer>

</main>
</body>
</html>
```